Harbor Loom Flooring Letterhead

Letterhead used for business reasons. It must be editable and easy to use.

Address is 5127 W. Pelican Lane Port Alder FL 30917 - 555.538.2194

```html
<!DOCTYPE html>
<html lang="en">
<head>
<meta charset="utf-8">
<title>Harbor Loom Flooring Letterhead</title>
<link href="https://fonts.googleapis.com/css2?family=Open+Sans:wght@400;600&family=Lato:wght@400&family=Manrope:wght@600&display=swap" rel="stylesheet">
<style>
  :root {
    --orange: #e08a26;
    --text-gray: #6e6e6e;
    --meta-gray: #8a8178;
    --dark: #2e2e2e;
    --rule: #8f8c84;
    --band-gray: #978e88;
    --paper: #ffffff;
  }
  html, body { margin: 0; padding: 0; overflow: hidden; background: var(--paper); }
  .letterhead {
    position: relative; width: 999px; height: 1200px; overflow: hidden;
    background: var(--paper);
    font-family: "Open Sans", Arial, sans-serif;
  }
  .brand-name {
    position: absolute; left: 70px; top: 86px; margin: 0;
    font-size: 34px; font-weight: 600; color: var(--orange); letter-spacing: 0.2px;
  }
  .company-contact {
    position: absolute; left: 682px; top: 90px;
    font-family: "Lato", Arial, sans-serif; font-size: 14.5px; color: var(--meta-gray);
    line-height: 17px;
  }
  .contact-row { display: flex; align-items: flex-start; gap: 6px; margin-bottom: 10px; }
  .contact-icon { width: 17px; height: 17px; flex: none; }
  .header-rule {
    position: absolute; left: 70px; top: 185px; width: 855px; height: 0;
    border-top: 1.5px solid var(--rule);
  }
  .sender { position: absolute; left: 89px; top: 301px; }
  .sender-name { margin: 0; font-size: 25px; font-weight: 600; color: var(--orange); line-height: 32px; }
  .sender-title { margin: 0; font-size: 13px; color: #555; line-height: 18px; }
  .sender-details { margin: 17px 0 0; padding: 0; list-style: none; font-size: 15.5px; color: #555; }
  .sender-details li { line-height: 24px; }
  .detail-label { display: inline-block; width: 33px; color: var(--orange); font-weight: 600; }
  .letter-date {
    position: absolute; right: 89px; top: 427px;
    font-size: 15.5px; color: #555;
  }
  .letter-body {
    position: absolute; left: 90px; top: 500px; width: 820px;
    font-size: 15.6px; line-height: 22.5px; color: var(--text-gray);
  }
  .letter-body p { margin: 0 0 22px; text-align: justify; text-align-last: left; }
  .signature-mark {
    position: absolute; left: 105px; top: 866px; width: 150px; height: 74px;
    background: linear-gradient(90deg, #f3f3f3, #ebebeb); border-radius: 4px;
  }
  .signatory {
    position: absolute; left: 90px; top: 954px; margin: 0;
    font-family: "Manrope", Arial, sans-serif; font-size: 22px; font-weight: 600; color: var(--dark);
  }
  .footer-bands { position: absolute; left: 0; bottom: 0; width: 999px; height: 45px; }
</style>
</head>
<body>
<div class="letterhead">
  <header>
    <h1 class="brand-name">Harbor Loom Flooring</h1>
    <div class="company-contact">
      <div class="contact-row">
        <svg class="contact-icon" viewBox="0 0 17 17" aria-hidden="true">
          <rect width="17" height="17" rx="2" fill="var(--orange)"/>
          <path d="M5.2 3.6l1.8 0.4 0.8 2.4-1.2 1c0.6 1.3 1.6 2.3 2.9 2.9l1-1.2 2.4 0.8 0.4 1.8c-0.4 0.9-1.3 1.4-2.2 1.3C7.6 12.6 4.4 9.4 3.9 5.8c-0.1-0.9 0.4-1.8 1.3-2.2z" fill="#fff"/>
        </svg>
        <span>555.538.2194</span>
      </div>
      <div class="contact-row">
        <svg class="contact-icon" viewBox="0 0 17 17" aria-hidden="true">
          <rect width="17" height="17" rx="2" fill="var(--orange)"/>
          <path d="M8.5 2.8a3.9 3.9 0 0 0-3.9 3.9c0 2.9 3.9 7.4 3.9 7.4s3.9-4.5 3.9-7.4a3.9 3.9 0 0 0-3.9-3.9z" fill="#fff"/>
          <circle cx="8.5" cy="6.7" r="1.5" fill="var(--orange)"/>
        </svg>
        <span>5127 W. Pelican Lane Port Alder<br>FL 30917</span>
      </div>
    </div>
    <div class="header-rule"></div>
  </header>

  <section class="sender">
    <h2 class="sender-name">Evan Marlowe</h2>
    <p class="sender-title">Chief Director</p>
    <ul class="sender-details">
      <li><span class="detail-label">A :</span>2210 Tidewater Avenue, Marrow Bay, FL 30942</li>
      <li><span class="detail-label">W :</span>www.harborloomflooring.com</li>
      <li><span class="detail-label">P :</span>+00 123 456 78</li>
      <li><span class="detail-label">M :</span>hello@harborloomflooring.com</li>
    </ul>
  </section>
  <div class="letter-date">12 December, 2025</div>

  <main class="letter-body">
    <p>Lorem ipsum dolor sit amet, consectetuer adipiscing elit, sed diam nonummy nibh euismod tincidunt ut laoreet dolore magna aliquam erat volutpat. Ut wisi enim ad minim veniam, quis nostrud exerci tation ullamcorper suscipit lobortis nisl ut aliquip ex ea commodo consequat. Duis autem vel eum iriure dolor in hendrerit in vulputate velit esse molestie consequat, vel illum dolore eu feugiat nulla facilisis at vero eros et accumsan et iusto odio dignissim qui blandit praesent luptatum zzril delenit augue duis dolore te feugait nulla facilisi.</p>
    <p>Lorem ipsum dolor sit amet, cons ectetuer adipiscing elit, sed diam nonummy nibh euismod tincidunt ut laoreet dolore magna aliquam erat volutpat. Ut wisi enim ad minim veniam, quis nostrud exerci tation ullamcorper suscipit lobortis nisl ut aliquip ex ea commodo consequat.</p>
    <p>Lorem ipsum dolor sit amet, consectetuer adipiscing elit, sed diam nonummy nibh euismod tincidunt ut laoreet dolore magna aliquam eratveniam, quis nostrud exerci tation ullamcorper suscipit lobortis nisl ut aliquip ex ea commodo consequat. Lorem ipsum dolor sit zamet, consectetuer adipiscing elit, sed diam nonummy nibh euismod tincidunt.</p>
  </main>

  <div class="signature-mark" role="img" aria-label="Handwritten signature of the signatory"></div>
  <p class="signatory">Mr. Dale Whitfield</p>

  <svg class="footer-bands" viewBox="0 0 999 45" aria-hidden="true">
    <polygon points="0,20 838,20 829,29 0,29" fill="var(--orange)"/>
    <polygon points="0,36 820,36 852,6 999,6 999,45 0,45" fill="var(--band-gray)"/>
  </svg>
</div>
</body>
</html>
```